Business Card for Fashion House

We need a business card design for our personalize fashion service for our customers. the business card should reflect reliability, luxury and creativity.
The brand Gravetto is extracted from "Graceful Vetto"; Gravetto provides fashion designs sprinkled with luxury and style tailored for our elite clients character profile.
Gravetto is created for those who embody class and elegance with a passion for style.
Target Market(s)
Affluent Customers
Industry/Entity Type
Fashion
Contact Information for Business Card
Rania Bou Khalil
Fashion Designer
Telephone: +971 5550123
Mobile +971 555987
Emal q@z.com
Website www.gravetto-example.com
Social Media Youtube g+ Facebook Instagram Pin /gravetto
Font styles to use
Other font styles liked:
- Audrey provided
Look and feel
Each slider illustrates characteristics of the customer's brand and the style your logo design should communicate.

```html
<!DOCTYPE html>
<html lang="en">
<head>
<meta charset="utf-8">
<title>Gravetto Business Card</title>
<link rel="stylesheet" href="https://fonts.googleapis.com/css2?family=Cormorant+Garamond:wght@400;500&family=Lato:wght@400;700&display=swap">
<style>
  :root {
    --bg: #2b2d30;
    --ink: #0a0a0a;
    --paper: #ffffff;
    --muted: #2a2a2a;
  }
  * { margin: 0; padding: 0; box-sizing: border-box; }
  html, body { width: 1200px; height: 900px; overflow: hidden; }
  body { background: var(--bg); position: relative; font-family: "Lato", sans-serif; }

  .card { position: absolute; border-radius: 24px; overflow: hidden; }

  /* Front: black portrait */
  .card-front { left: 120px; top: 170px; width: 320px; height: 560px; background: var(--ink); }
  .front-brand { position: absolute; top: 130px; left: 0; right: 0; text-align: center; color: var(--paper); }
  .brand-mark { display: block; margin: 0 auto 18px; width: 40px; height: 40px; border-radius: 50%; border: 3px solid currentColor; }
  .brand-name { font-family: "Cormorant Garamond", serif; font-weight: 400; font-size: 26px; letter-spacing: 9px; padding-left: 9px; }
  .social-row { position: absolute; top: 272px; left: 0; right: 0; display: flex; justify-content: center; gap: 14px; }
  .social-slot { width: 20px; height: 20px; background: var(--paper); border-radius: 4px; }
  .front-band { position: absolute; left: 0; right: 0; top: 436px; height: 60px; background: var(--paper); }

  /* Back: white landscape */
  .card-back { left: 510px; top: 310px; width: 560px; height: 320px; background: var(--paper); }
  .back-band { position: absolute; top: 0; bottom: 0; left: 30px; width: 30px; background: var(--ink); }
  .back-brand { position: absolute; left: 96px; top: 36px; color: var(--ink); text-align: center; }
  .back-brand .brand-mark { width: 30px; height: 30px; border-width: 2.5px; margin-bottom: 10px; }
  .back-brand .brand-name { font-size: 17px; letter-spacing: 6px; }
  .rule-top { position: absolute; height: 2px; background: var(--ink); left: 140px; right: 0; top: 118px; }

  .details { position: absolute; left: 300px; right: 60px; top: 150px; color: var(--ink); }
  .holder { text-align: right; }
  .holder-name { font-weight: 700; font-size: 20px; line-height: 1.2; }
  .holder-role { font-family: "Cormorant Garamond", serif; font-size: 14px; line-height: 1.2; }
  .rule-bottom { height: 2px; background: var(--ink); margin: 8px 0 10px; }
  .contacts { display: grid; grid-template-columns: 30px auto; row-gap: 4px; color: var(--muted); font-size: 11.5px; line-height: 1.15; white-space: nowrap; }
  .contacts .big { font-size: 15px; letter-spacing: 0.5px; }

  .back-tab { position: absolute; right: 0; top: 248px; width: 32px; height: 30px; background: var(--ink); border-radius: 6px 0 0 6px; }
</style>
</head>
<body>
  <section class="card card-front">
    <div class="front-brand">
      <span class="brand-mark"></span>
      <span class="brand-name">GRAVETTO</span>
    </div>
    <div class="social-row">
      <span class="social-slot"></span>
      <span class="social-slot"></span>
      <span class="social-slot"></span>
      <span class="social-slot"></span>
    </div>
    <div class="front-band"></div>
  </section>

  <section class="card card-back">
    <div class="back-band"></div>
    <div class="back-brand">
      <span class="brand-mark"></span>
      <span class="brand-name">GRAVETTO</span>
    </div>
    <div class="rule-top"></div>
    <div class="details">
      <div class="holder">
        <p class="holder-name">Rania Bou Khalil</p>
        <p class="holder-role">Fashion Designer</p>
      </div>
      <div class="rule-bottom"></div>
      <dl class="contacts">
        <dt class="big">T :</dt><dd class="big">+971 5550123</dd>
        <dt class="big">M :</dt><dd class="big">+971 555987</dd>
        <dt>E :</dt><dd>q@z.com</dd>
        <dt>W :</dt><dd>www.gravetto-example.com</dd>
      </dl>
    </div>
    <div class="back-tab"></div>
  </section>
</body>
</html>
```